brixtane motor oil

I would like to inform you that our new motor oil brand brixtane will be divided into three categories:
Brixtane high performance Full Synthetic
0w20 ,5w30 ,0w16,5w20
with massage.
Maximum Protection, Ultimate Performance.brixtane quendor
--------------------------------
brixtane quendor Synthetic Blend
10w40,5w30,5w20
with massage
The perfect combination of durability and efficiency
-------------------------------
brixtane gelvoria transmission fluid
ATF III
with massage
proven to maximize transmission life

```html
<!DOCTYPE html>
<html lang="en">
<head>
<meta charset="utf-8">
<title>Brixtane Quendor Synthetic Blend – Label</title>
<link rel="stylesheet" href="https://fonts.googleapis.com/css2?family=Archivo+Black&family=Exo+2:ital,wght@1,900&family=Roboto:wght@400&display=swap">
<style>
  :root {
    --backdrop: #15191c;
    --label-white: #f4f6f8;
    --sky-blue: #8fc6ec;
    --stripe-blue: #2c8fd6;
    --navy: #0f2a5e;
    --navy-deep: #0a1c44;
    --ink: #0b0b0b;
    --text-white: #ffffff;
    --rule-blue: #9cc8ee;
    --chrome-edge: #1a1f26;
    --photo-gold: #b98a2c;
    --photo-steel: #5b6673;
  }
  html, body {
    margin: 0;
    width: 1200px;
    height: 927px;
    overflow: hidden;
    background: var(--backdrop);
  }
  .canvas {
    position: relative;
    width: 1200px;
    height: 927px;
  }
  .label {
    position: absolute;
    left: 277px;
    top: 44px;
    width: 647px;
    height: 840px;
    display: block;
  }
  .brand-mark { font-family: "Archivo Black", sans-serif; fill: var(--navy); }
  .brand-name { font-family: "Archivo Black", sans-serif; fill: var(--text-white); letter-spacing: 1px; }
  .product-name { font-family: "Exo 2", sans-serif; font-style: italic; font-weight: 900; }
  .product-name-edge { fill: var(--chrome-edge); }
  .product-type { font-family: "Archivo Black", sans-serif; fill: var(--text-white); }
  .grade { font-family: "Exo 2", sans-serif; font-style: italic; font-weight: 900; fill: var(--ink); }
  .tagline { font-family: "Roboto", sans-serif; fill: var(--text-white); }
</style>
</head>
<body>
<main class="canvas">
  <svg class="label" viewBox="0 0 520 675" xmlns="http://www.w3.org/2000/svg" aria-label="Brixtane Quendor Synthetic Blend 10w40 1L label">
    <defs>
      <linearGradient id="topBand" x1="0" y1="0" x2="1" y2="0">
        <stop offset="0" stop-color="var(--label-white)"/>
        <stop offset="0.6" stop-color="#dfeef9"/>
        <stop offset="1" stop-color="var(--sky-blue)"/>
      </linearGradient>
      <radialGradient id="navyPanel" cx="0.55" cy="0.35" r="0.8">
        <stop offset="0" stop-color="#1d4a8f"/>
        <stop offset="1" stop-color="var(--navy-deep)"/>
      </radialGradient>
      <linearGradient id="chrome" x1="0" y1="0" x2="0" y2="1">
        <stop offset="0" stop-color="#ffffff"/>
        <stop offset="0.45" stop-color="#c3c8ce"/>
        <stop offset="0.55" stop-color="#767d85"/>
        <stop offset="1" stop-color="#eceef0"/>
      </linearGradient>
      <linearGradient id="photoTone" x1="0" y1="0" x2="1" y2="0.3">
        <stop offset="0" stop-color="var(--photo-gold)"/>
        <stop offset="0.45" stop-color="#8a6a35"/>
        <stop offset="1" stop-color="var(--photo-steel)"/>
      </linearGradient>
    </defs>

    <rect class="top-band" x="0" y="0" width="520" height="200" fill="url(#topBand)"/>
    <text class="brand-mark" x="460" y="62" font-size="18" text-anchor="middle">brixtane</text>

    <path class="curve-stripe" d="M0,112 Q210,40 520,160 L520,200 Q210,70 0,130 Z" fill="var(--stripe-blue)"/>
    <path class="navy-panel" d="M0,128 Q210,68 520,196 L520,675 L0,675 Z" fill="url(#navyPanel)"/>

    <text class="brand-name" x="112" y="162" font-size="22">BRIXTANE</text>

    <g transform="rotate(-8 240 280)">
      <text class="product-name product-name-edge" x="51" y="293" font-size="92">Quendor</text>
      <text class="product-name" x="48" y="290" font-size="92" fill="url(#chrome)">Quendor</text>
      <line x1="130" y1="312" x2="420" y2="312" stroke="var(--rule-blue)" stroke-width="2"/>
      <text class="product-type" x="78" y="352" font-size="32">Synthetic Blend</text>
      <line x1="130" y1="366" x2="360" y2="366" stroke="var(--rule-blue)" stroke-width="1.5"/>
    </g>

    <rect class="photo-area" x="0" y="405" width="520" height="245" fill="url(#photoTone)" role="img" aria-label="Photo of golden motor oil splashing over steel engine gears"/>

    <rect class="grade-box" x="285" y="470" width="235" height="120" fill="var(--label-white)"/>
    <text class="grade" x="505" y="525" font-size="50" text-anchor="end">10w40</text>
    <text class="grade" x="490" y="575" font-size="38" text-anchor="end">1L</text>

    <text class="tagline" x="232" y="609" font-size="10">The perfect combination of durability</text>
    <text class="tagline" x="232" y="622" font-size="10">and efficiency.</text>

    <rect class="bottom-strip" x="0" y="650" width="520" height="25" fill="var(--navy-deep)"/>
  </svg>
</main>
</body>
</html>
```